Donation Brochure for Ashgrove Meadow Hospital Foundation

We are the Ashgrove Meadow Hospital Foundation in Montreal, Quebec, Canada

We need a brochure that people can fill out in order to make a donation to the Foundation.

The brochure NEEDS TO BE BILINGUAL (English and French) and include a return envelope that can be ripped off from the main brochure, and then sealed with the donation inside.

Please no pictures of buildings, only people.

I have uploaded files to show which fields must be present for donors to fill out.

Target Market(s)

Most of our donors are over the age of 60. 70% Anglophone, 30% Francophone

Industry/Entity Type

Hospital

Requirements
Must have
• Our logo (included in files)

contact info for foundation:

342 Birchwell Ave East, B3.12
Montreal, QC H2K 4B7
Tel: 514-726-3908
Fax: 514-726-3951
email: hope@ashmeadfdn.org
web: ashmeadfdn.org

Return envelope

BILINGUAL
Should not have
• Pictures of buildings

```html
<!DOCTYPE html>
<html lang="en">
<head>
<meta charset="utf-8">
<title>Ashgrove Meadow Hospital Foundation – Donation Form</title>
<link href="https://fonts.googleapis.com/css2?family=Source+Sans+3:ital,wght@0,400;0,600;0,700;1,400&display=swap" rel="stylesheet">
<style>
  :root{
    --navy:#1d4f8e;
    --ink:#2b2b2b;
    --rule:#6a6a6a;
    --gift:#f6e5a3;
    --pay:#bdd1e5;
    --gold:#f0cf63;
    --paper:#ffffff;
    --stage:#ffffff;
  }
  *{box-sizing:border-box;margin:0;padding:0}
  html,body{width:1200px;height:900px;overflow:hidden;background:var(--stage)}
  body{position:relative;font-family:"Source Sans 3",Arial,sans-serif;color:var(--ink)}

  .sheet{
    position:absolute;left:276.5px;top:-156.5px;width:647px;height:1170px;
    background:var(--paper);transform:rotate(-90deg);transform-origin:center;
    box-shadow:0 0 6px rgba(0,0,0,.22);
  }
  .perf-v{position:absolute;top:0;height:875px;border-left:1px dashed #777}
  .perf-h{position:absolute;left:0;right:0;top:875px;border-top:1px dashed #777}
  .perf-mid{position:absolute;left:0;right:0;top:585px;border-top:1px dotted #999}
  .perf-label{position:absolute;font-style:italic;font-size:7px;line-height:7px;color:var(--navy);white-space:nowrap}
  .perf-label.top{left:634px;top:465px;transform-origin:0 0;transform:rotate(-90deg)}
  .perf-label.fold{left:14px;top:879px}

  .col{position:absolute;top:0;height:875px}
  .col.fr{left:12px;width:300px}
  .col.en{left:328px;width:295px}

  .gift-panel{position:absolute;left:0;right:0;top:190px;height:360px;background:var(--gift)}
  .pay-panel{position:absolute;left:0;right:0;top:707px;height:153px;background:var(--pay)}

  .heading{position:absolute;left:0;font-weight:700;font-size:10.5px;color:var(--navy);white-space:nowrap}
  .heading small{font-weight:400;font-size:4.6px;color:var(--ink)}

  .field{position:absolute;left:0;right:0;height:10px;display:flex;align-items:flex-end;font-size:5.6px;gap:2px}
  .field.inset{left:8px;right:8px}
  .field .line{flex:1;border-bottom:.7px dotted var(--rule);height:6px}
  .field .pair{display:flex;flex:1;align-items:flex-end;gap:2px}
  .field small{font-size:4.2px}
  .divider{position:absolute;left:0;right:0;border-top:.7px dotted var(--rule)}

  .check{position:absolute;display:flex;align-items:center;gap:4px;font-size:5.8px;white-space:nowrap}
  .box{width:11px;height:11px;border:.8px solid #333;border-radius:2px;background:#fff;flex:none}
  .amount{width:28px;height:18px;border:.8px solid #333;border-radius:3px;background:#fff;font-size:5.6px;padding:2px 3px;display:flex;align-items:flex-end}
  .reg{position:absolute;left:8px;top:858px;font-size:3.6px;color:#444}

  .story{position:absolute;top:875px;height:295px}
  .story .heading{position:static;font-size:10px;line-height:11px;white-space:normal}
  .story p{font-size:6px;line-height:6.7px;margin:6px 0 9px}
  .angel-art{position:absolute;left:30px;top:912px;width:290px;height:80px;
    background:radial-gradient(ellipse at 55% 50%,rgba(240,207,99,.5),rgba(240,207,99,0) 70%)}
</style>
</head>
<body>
<div class="sheet">

  <div class="perf-v" style="left:630px"></div>
  <div class="perf-v" style="left:322px"></div>
  <div class="perf-h"></div>
  <div class="perf-mid"></div>
  <div class="perf-label top">Perforate Here</div>
  <div class="perf-label fold">Perforate Here</div>

  <div class="angel-art" role="img" aria-label="Soft golden guardian angel wing illustration behind the story text"></div>

  <section class="col fr" lang="fr">
    <div class="gift-panel"></div>
    <div class="pay-panel"></div>

    <h2 class="heading" style="top:22px">Renseignement Du Donateur <small>(Pour reçu d'impôts)</small></h2>
    <div class="field" style="top:46px">Nom:<span class="line"></span></div>
    <div class="field" style="top:71px">Adresse:<span class="line"></span></div>
    <div class="field" style="top:91px"><span class="line"></span></div>
    <div class="field" style="top:106px">Ville:<span class="line"></span></div>
    <div class="field" style="top:131px"><span class="pair">Province:<span class="line"></span></span><span class="pair">Code Postale:<span class="line"></span></span></div>
    <div class="field" style="top:151px">Courriel:<span class="line"></span></div>
    <div class="field" style="top:174px"><span class="pair">Tel Domicile:<span class="line"></span></span><span class="pair">Tel Cellulaire:<span class="line"></span></span></div>

    <h2 class="heading" style="left:8px;top:204px">J'aimerais faire mon don: <small>(Cochez une case seulement)</small></h2>
    <div class="field inset" style="top:228px">À la mémoire de:<span class="line"></span></div>
    <div class="field inset" style="top:248px">En l'honneur de:<span class="line"></span></div>
    <div class="field inset" style="top:271px">Occasion: <small>(Anniversaire, célébration, autres)</small><span class="line"></span></div>
    <div class="divider" style="top:290px"></div>
    <div class="field inset" style="top:296px">Le nom de mon Ange Gardien:<span class="line"></span></div>
    <div class="field inset" style="top:318px">Département:<span class="line"></span></div>
    <h2 class="heading" style="left:8px;top:341px">Prière d'envoyer un avis de mon don à:</h2>
    <div class="field inset" style="top:366px">Nom:<span class="line"></span></div>
    <div class="field inset" style="top:386px">Adresse:<span class="line"></span></div>
    <div class="field inset" style="top:408px"><span class="line"></span></div>
    <div class="field inset" style="top:431px">Ville:<span class="line"></span></div>
    <div class="field inset" style="top:451px"><span class="pair">Province:<span class="line"></span></span><span class="pair">Code Postale:<span class="line"></span></span></div>
    <div class="field inset" style="top:471px">Signataire de la notification:<span class="line"></span></div>
    <div class="field inset" style="top:491px">Message: <small>(Optionnel)</small><span class="line"></span></div>
    <div class="field inset" style="top:516px"><span class="line"></span></div>

    <h2 class="heading" style="top:565px">J'aimerais que mon don soit dédié:</h2>
    <div class="check" style="left:8px;top:589px"><span class="box"></span>Les besoins les plus urgents de l'Hôpital</div>
    <div class="check" style="left:8px;top:611px"><span class="box"></span>Autre</div>

    <h2 class="heading" style="top:632px">J'aimerais donner un montant de:</h2>
    <div class="check" style="left:8px;top:662px"><span class="box"></span>75$</div>
    <div class="check" style="left:64px;top:662px"><span class="box"></span>100$</div>
    <div class="check" style="left:128px;top:662px"><span class="box"></span>250$ Cercle des gouverneur</div>
    <div class="check" style="left:8px;top:686px"><span class="box"></span>Autre <span class="amount">$</span></div>

    <h2 class="heading" style="left:8px;top:717px">Mode de paiement</h2>
    <div class="check" style="left:8px;top:743px"><span class="box"></span>Chèque à l'ordre de la FONDATION DE L'HÔPITAL ASHGROVE MEADOW</div>
    <div class="check" style="left:8px;top:763px"><span class="box"></span>Vantra</div>
    <div class="check" style="left:52px;top:763px"><span class="box"></span>Meridian Card</div>
    <div class="check" style="left:120px;top:763px"><span class="box"></span>Amplex</div>
    <div class="field inset" style="top:796px">Titulaire de la carte:<span class="line"></span></div>
    <div class="field inset" style="top:819px">No de carte:<span class="line"></span></div>
    <div class="field inset" style="top:842px"><span class="pair">Date d'exp:<span class="line"></span></span><span class="pair">Signature:<span class="line"></span></span></div>
    <div class="reg">No. d'enregistrement 10457 3382 RR 0001</div>

    <article class="story" style="left:0;width:278px">
      <h3 class="heading" style="margin-top:23px">Avez-vous un Ange gardien?</h3>
      <p>Il arrive parfois que quelqu'un dépasse le simple cadre de ses attributions pour vous ou pour une personne que vous aimez – dans l'espoir d'ensoleiller votre journée, de faciliter votre rétablissement, de rendre votre séjour plus confortable… Qu'il s'agisse de la réceptionniste qui vous a accueilli avec un sourire, de l'infirmière qui est restée à votre chevet pendant tout son quart de travail, du chirurgien qui a sauvé la vie de votre mère ou du préposé qui a marché avec votre oncle dans le couloir…</p>
      <h3 class="heading">On trouve des Anges gardiens partout<br>à l'Hôpital Ashgrove Meadow!</h3>
      <p>Afin de manifester votre gratitude à l'un d'eux et de le remercier, prenez un moment pour l'honorer avec une épinglette exclusive l'identifiant en tant qu'Ange gardien. Votre geste attentionné constituera une manifestation d'encouragement et une tape sur l'épaule bien méritée pour les personnes qui se dévouent chaque jour pour nous et pour ceux qui nous sont chers. Votre appui sera d'ailleurs consacré aux priorités les plus urgentes de l'Hôpital Ashgrove Meadow afin de permettre à nos Anges gardiens de poursuivre leur travail extraordinaire.</p>
    </article>
  </section>

  <section class="col en" lang="en">
    <div class="gift-panel"></div>
    <div class="pay-panel"></div>

    <h2 class="heading" style="top:22px">Donor information <small>(For official income tax receipt)</small></h2>
    <div class="field" style="top:46px">Name:<span class="line"></span></div>
    <div class="field" style="top:71px">Address:<span class="line"></span></div>
    <div class="field" style="top:91px"><span class="line"></span></div>
    <div class="field" style="top:106px">City:<span class="line"></span></div>
    <div class="field" style="top:131px"><span class="pair">Province:<span class="line"></span></span><span class="pair">Postal Code:<span class="line"></span></span></div>
    <div class="field" style="top:151px">Email:<span class="line"></span></div>
    <div class="field" style="top:174px"><span class="pair">Home Phone:<span class="line"></span></span><span class="pair">Cell Phone:<span class="line"></span></span></div>

    <h2 class="heading" style="left:8px;top:204px">I would like to make my gift: <small>(Please check any one)</small></h2>
    <div class="field inset" style="top:228px">In Memory of:<span class="line"></span></div>
    <div class="field inset" style="top:248px">In Honour of:<span class="line"></span></div>
    <div class="field inset" style="top:271px">Occasion: <small>(Birthday, Anniversary, Get well soon, etc)</small><span class="line"></span></div>
    <div class="divider" style="top:290px"></div>
    <div class="field inset" style="top:296px">My Guardians Angel's name:<span class="line"></span></div>
    <div class="field inset" style="top:318px">Department:<span class="line"></span></div>
    <h2 class="heading" style="left:8px;top:341px">Please send notification of my gift to:</h2>
    <div class="field inset" style="top:366px">Name:<span class="line"></span></div>
    <div class="field inset" style="top:386px">Address:<span class="line"></span></div>
    <div class="field inset" style="top:408px"><span class="line"></span></div>
    <div class="field inset" style="top:431px">City:<span class="line"></span></div>
    <div class="field inset" style="top:451px"><span class="pair">Province:<span class="line"></span></span><span class="pair">Postal Code:<span class="line"></span></span></div>
    <div class="field inset" style="top:471px">Notification card from:<span class="line"></span></div>
    <div class="field inset" style="top:491px">Message: <small>(Optional)</small><span class="line"></span></div>
    <div class="field inset" style="top:516px"><span class="line"></span></div>

    <h2 class="heading" style="top:565px">I would like my donation to benefit:</h2>
    <div class="check" style="left:8px;top:589px"><span class="box"></span>The most urgent needs of the Hospital</div>
    <div class="check" style="left:8px;top:611px"><span class="box"></span>Other</div>

    <h2 class="heading" style="top:632px">I would like to make a donation of:</h2>
    <div class="check" style="left:8px;top:662px"><span class="box"></span>$75</div>
    <div class="check" style="left:64px;top:662px"><span class="box"></span>$100</div>
    <div class="check" style="left:128px;top:662px"><span class="box"></span>$250 Governors' Circle</div>
    <div class="check" style="left:8px;top:686px"><span class="box"></span>Other <span class="amount">$</span></div>

    <h2 class="heading" style="left:8px;top:717px">Method of payment</h2>
    <div class="check" style="left:8px;top:743px"><span class="box"></span>Cheque made payable to the ASHGROVE MEADOW HOSPITAL FOUNDATION</div>
    <div class="check" style="left:8px;top:763px"><span class="box"></span>Vantra</div>
    <div class="check" style="left:52px;top:763px"><span class="box"></span>Meridian Card</div>
    <div class="check" style="left:120px;top:763px"><span class="box"></span>Amplex</div>
    <div class="field inset" style="top:796px">Cardholder's Name:<span class="line"></span></div>
    <div class="field inset" style="top:819px">Card Number:<span class="line"></span></div>
    <div class="field inset" style="top:842px"><span class="pair">Expiry Date:<span class="line"></span></span><span class="pair">Signature:<span class="line"></span></span></div>
    <div class="reg">Registration # 10457 3382 RR 0001</div>

    <article class="story" style="left:0;width:278px">
      <h3 class="heading" style="margin-top:23px">Do you have a Guardian Angel?</h3>
      <p>Every once in a while, someone goes above and beyond the call of duty – for you or your someone you love – in the hopes of making your day brighter, your recovery easier, your stay more comfortable… Whether it's the receptionist who greeted you with a smile, the nurse who stood by your side during his entire stay, the surgeon who saved your mother's life, or the orderly who walked alongside your uncle in the hall…</p>
      <h3 class="heading">Guardian Angels are everywhere at<br>the Ashgrove Meadow Hospital!</h3>
      <p>To show your gratitude and give thanks to someone, take a moment to honour them with a unique lapel pin identifying him or her as a Guardian Angel. Your thoughtful gesture will be a call of encouragement and well-deserved pat on the back for the people who dedicate themselves everyday to us and to those we hold so dear. And your support will go directly toward the Ashgrove Meadow Hospital's most urgent priorities, to empower our Guardian Angels to continue their incredible work.</p>
    </article>
  </section>
</div>
</body>
</html>
```